Brisk Mend's Blow Their Mind Website

We own a group of cell phone and tablet repair shops in the bay area that is emerging into the mobile device insurance industry and want to develop a site that is clean, organized, and efficient at communicating who we are, the services we provide and the positive feedback we have been getting from our clients. As we enter into this new field of business, Our goal is to attract larger corporate accounts.

We want our home screen to have a big focus on the protection plan for the devices right away much like the home screen from these links:

http://www.gadgetvault.com/

and also - https://us.keepitsnug.com/smartphone-protection.html

We also need to make our repair services clear, here is a website of a company that does repair and we want to highlight both ends of the business.

ww.fixnovo.com

So the home screen will include the tab categories at the top of the screen
home/ protection /repair /about /contact

The first portion will be protection and as you scroll down there will be the next section about repair and following that will be information about the company.

Target Market(s)

Individuals that would be looking for pricing, clients that come to our store, but ultimately the heavy hitters we would want to attract would be larger corporate accounts so the message we want to communicate is professional, organized and credible in the services we provide.

Industry/Entity Type

Cell Phone

Number of Pages Required

5+ page

Font styles to use
Serif

Colors
34a6d7

Requirements
Must have
• Eye catching, organized, with the wow factor that a business will look at our site and will be able to tell that we know what looks good and what grabs peoples attention. A large emphasis on the protection plan section like the links we provided and an organized home screen with the sections highlighted in the project description
• Tabs with links to different sections of the business such as protection that will go into detail about our protections plans and why our plan is best
• repair with a menu of the different prices we provide for different devices and services for that device
• an about us tab
• a contact us tab
Nice to have
• Artistic flow on the homescreen that the different sections flow together without looking too cookie cutter
• Wow factor
Should not have
• Clutter, confusion, disorganization, cheesy cookie cutter

```html
<!DOCTYPE html>
<html lang="en">
<head>
<meta charset="utf-8">
<title>Brisk Mend – Phone &amp; Tablet Repair and Protection</title>
<link href="https://fonts.googleapis.com/css2?family=Open+Sans:wght@400;600;700;800&display=swap" rel="stylesheet">
<style>
:root{
  --blue:#29a9e1;
  --blue-deep:#1b8fc6;
  --ink:#333a40;
  --muted:#8a9298;
  --light:#f3f5f7;
  --white:#ffffff;
  --footer:#3b3f44;
  --star:#f4b400;
}
*{box-sizing:border-box;margin:0;padding:0}
html,body{width:682px;height:1200px;overflow:hidden}
body{font-family:"Open Sans",Arial,sans-serif;color:var(--ink);background:var(--white);position:relative}

/* header */
.site-header{height:40px;display:flex;align-items:center;justify-content:space-between;padding:0 34px 0 40px;background:var(--white)}
.brand{display:flex;align-items:center;gap:7px;font-weight:700;font-size:17px;color:var(--ink)}
.brand-mark{width:16px;height:16px;background:var(--blue)}
.header-right{display:flex;flex-direction:column;align-items:flex-end;gap:3px}
.utility{display:flex;align-items:center;gap:4px;font-size:6px;color:var(--ink)}
.social-dot{width:8px;height:8px;border-radius:50%;background:#6c7378}
.utility .acct{margin-left:6px;padding:1px 5px;background:var(--ink);color:var(--white);font-weight:600}
.main-nav{display:flex;gap:2px}
.main-nav a{font-size:7px;font-weight:600;color:var(--ink);text-decoration:none;padding:5px 11px}
.main-nav a.active{background:var(--blue);color:var(--white)}

/* hero */
.hero{position:relative;height:222px;overflow:hidden}
.hero-photo{position:absolute;inset:0;background:linear-gradient(110deg,#556572 0%,#8d9aa3 45%,#c9cfd3 70%,#7e8a93 100%)}
.hero-panel{position:absolute;left:0;top:0;width:300px;height:100%;background:rgba(41,169,225,.88);padding:26px 0 0 40px;color:var(--white)}
.hero-panel h1{font-size:14px;font-weight:800;letter-spacing:.3px;margin-bottom:8px}
.checklist{display:grid;grid-template-columns:110px 120px;row-gap:5px;list-style:none;font-size:7.5px}
.checklist li{display:flex;align-items:center;gap:5px}
.checklist svg{flex:none}
.btn-dark{display:inline-block;margin-top:20px;background:#243038;color:var(--white);font-size:6.5px;font-weight:600;padding:5px 10px}
.price-box{position:absolute;left:420px;top:128px;color:var(--white)}
.price-box .from{font-size:8px;font-weight:600}
.price-box .from strong{font-size:17px;font-weight:700}
.price-box .from small{font-size:8px}
.price-box .quote{display:inline-block;margin-top:3px;background:var(--blue);font-size:6.5px;padding:4px 8px}
.price-box .compare{display:block;margin-top:6px;font-size:8px;font-weight:600}

/* services */
.services{height:228px;padding-top:20px;background:var(--white)}
.section-title{text-align:center;font-size:12px;font-weight:800;letter-spacing:.2px}
.section-title::after{content:"";display:block;width:40px;height:2px;background:var(--blue);margin:6px auto 0}
.services-body{display:flex;margin-top:14px;padding-left:50px}
.device-art{width:220px;height:150px;background:linear-gradient(160deg,#eef1f3,#cfd6db);border-radius:6px}
.service-grid{display:grid;grid-template-columns:150px 150px;column-gap:16px;row-gap:11px;margin-left:44px}
.service{display:flex;gap:7px}
.service-icon{flex:none;width:22px;height:22px;border-radius:50%;border:1.5px solid var(--blue);display:flex;align-items:center;justify-content:center}
.service h3{font-size:8px;font-weight:700;color:var(--blue)}
.service p{font-size:5.5px;color:var(--muted);line-height:1.4;margin-top:1px}

/* walk in band */
.walkin{height:210px;background:var(--blue);color:var(--white);text-align:center;padding-top:20px}
.walkin h2{font-size:11px;font-weight:800}
.walkin .sub{font-size:6px;margin-top:3px;opacity:.85}
.device-row{display:flex;justify-content:center;gap:54px;margin-top:16px}
.device{display:flex;flex-direction:column;align-items:center}
.device-shot{background:linear-gradient(180deg,#2b2f33,#4a5259);border-radius:6px;border:3px solid #e9edf0}
.device span{font-size:6.5px;font-weight:700;margin-top:8px}

/* testimonials */
.reviews{height:220px;background:var(--light);padding-top:22px}
.review-row{display:flex;justify-content:center;gap:26px;margin-top:18px}
.review{width:112px;height:112px;border-radius:50%;background:var(--white);border:1px solid #dde2e6;display:flex;flex-direction:column;align-items:center;justify-content:center;text-align:center;padding:0 14px}
.stars{color:var(--star);font-size:9px;letter-spacing:1px}
.review p{font-size:5.5px;color:var(--muted);line-height:1.45;margin-top:5px}
.review a{font-size:5.5px;color:var(--blue);font-weight:700;margin-top:5px;text-decoration:none}

/* who we are */
.about{height:230px;background:var(--blue);color:var(--white);display:flex;padding:22px 34px 0 40px;gap:24px}
.about-text{width:310px}
.about-text h2{font-size:14px;font-weight:800;margin-bottom:8px}
.about-text p{font-size:6.3px;line-height:1.6;margin-bottom:7px}
.about-text .btn-dark{margin-top:6px}
.about-photo{width:274px;height:180px;background:linear-gradient(135deg,#e8d9c6,#bfa58a 55%,#7d8c96)}

/* footer */
.site-footer{height:50px;background:var(--footer);color:#c9ced2;display:flex;align-items:center;justify-content:space-between;padding:0 34px 0 40px}
.footer-links{display:flex;gap:12px;font-size:6px}
.site-footer .brand{color:var(--white);font-size:13px}
</style>
</head>
<body>

<header class="site-header">
  <div class="brand"><span class="brand-mark"></span>Brisk Mend</div>
  <div class="header-right">
    <div class="utility">
      <span class="social-dot"></span><span class="social-dot"></span><span class="social-dot"></span><span class="social-dot"></span><span class="social-dot"></span>
      <span class="acct">Login</span><span class="acct">Register</span>
    </div>
    <nav class="main-nav">
      <a class="active" href="#">HOME</a>
      <a href="#">ABOUT US</a>
      <a href="#">REPAIR</a>
      <a href="#">PROTECT</a>
      <a href="#">CONTACT</a>
    </nav>
  </div>
</header>

<section class="hero">
  <div class="hero-photo" role="img" aria-label="Photo of a young man in a suit holding a smartphone and cheering"></div>
  <div class="hero-panel">
    <h1>PEACE OF MIND</h1>
    <ul class="checklist">
      <li><svg width="7" height="7" viewBox="0 0 10 10"><path d="M1 5l3 3 5-6" stroke="#fff" stroke-width="1.8" fill="none"/></svg>Cracked Screens</li>
      <li><svg width="7" height="7" viewBox="0 0 10 10"><path d="M1 5l3 3 5-6" stroke="#fff" stroke-width="1.8" fill="none"/></svg>Battery Replacement</li>
      <li><svg width="7" height="7" viewBox="0 0 10 10"><path d="M1 5l3 3 5-6" stroke="#fff" stroke-width="1.8" fill="none"/></svg>Broken LCD's</li>
      <li><svg width="7" height="7" viewBox="0 0 10 10"><path d="M1 5l3 3 5-6" stroke="#fff" stroke-width="1.8" fill="none"/></svg>Unlocking / unlocking service</li>
      <li><svg width="7" height="7" viewBox="0 0 10 10"><path d="M1 5l3 3 5-6" stroke="#fff" stroke-width="1.8" fill="none"/></svg>Charging Ports</li>
      <li><svg width="7" height="7" viewBox="0 0 10 10"><path d="M1 5l3 3 5-6" stroke="#fff" stroke-width="1.8" fill="none"/></svg>Flashing</li>
      <li><svg width="7" height="7" viewBox="0 0 10 10"><path d="M1 5l3 3 5-6" stroke="#fff" stroke-width="1.8" fill="none"/></svg>No sound / low audio</li>
      <li><svg width="7" height="7" viewBox="0 0 10 10"><path d="M1 5l3 3 5-6" stroke="#fff" stroke-width="1.8" fill="none"/></svg>Volume Button</li>
      <li><svg width="7" height="7" viewBox="0 0 10 10"><path d="M1 5l3 3 5-6" stroke="#fff" stroke-width="1.8" fill="none"/></svg>Water Damage</li>
      <li><svg width="7" height="7" viewBox="0 0 10 10"><path d="M1 5l3 3 5-6" stroke="#fff" stroke-width="1.8" fill="none"/></svg>Power Button</li>
    </ul>
    <span class="btn-dark">Enter More</span>
  </div>
  <div class="price-box">
    <div class="from">From <strong>$5.99</strong> <small>/ month</small></div>
    <span class="quote">Get a quote in 30 seconds</span>
    <span class="compare">Price comparison Chart</span>
  </div>
</section>

<section class="services">
  <h2 class="section-title">INTRODUCING TO REPAIR SERVICES</h2>
  <div class="services-body">
    <div class="device-art" role="img" aria-label="Illustration of a smartphone with callout points marking repairable parts"></div>
    <div class="service-grid">
      <div class="service"><span class="service-icon"><svg width="10" height="12" viewBox="0 0 10 12"><rect x="1.5" y="0.5" width="7" height="11" rx="1" stroke="#29a9e1" fill="none"/></svg></span><div><h3>Cracked Screens</h3><p>Quick repair by certified techs using genuine parts.</p></div></div>
      <div class="service"><span class="service-icon"><svg width="10" height="12" viewBox="0 0 10 12"><rect x="1.5" y="0.5" width="7" height="11" rx="1" stroke="#29a9e1" fill="none"/></svg></span><div><h3>Broken LCD's</h3><p>Quick repair by certified techs using genuine parts.</p></div></div>
      <div class="service"><span class="service-icon"><svg width="10" height="10" viewBox="0 0 10 10"><path d="M6 0L2 6h3l-1 4 4-6H5z" fill="#29a9e1"/></svg></span><div><h3>Flashing</h3><p>Quick repair by certified techs using genuine parts.</p></div></div>
      <div class="service"><span class="service-icon"><svg width="12" height="8" viewBox="0 0 12 8"><rect x="0.5" y="0.5" width="9" height="7" stroke="#29a9e1" fill="none"/><rect x="10" y="2.5" width="1.5" height="3" fill="#29a9e1"/></svg></span><div><h3>Battery Replacement</h3><p>Quick repair by certified techs using genuine parts.</p></div></div>
      <div class="service"><span class="service-icon"><svg width="8" height="11" viewBox="0 0 8 11"><path d="M4 0C4 0 0 5 0 7a4 4 0 008 0C8 5 4 0 4 0z" fill="#29a9e1"/></svg></span><div><h3>Water Damage</h3><p>Quick repair by certified techs using genuine parts.</p></div></div>
      <div class="service"><span class="service-icon"><svg width="11" height="10" viewBox="0 0 11 10"><path d="M0 3h3l3-3v10L3 7H0z" fill="#29a9e1"/><path d="M8 3l3 4M11 3l-3 4" stroke="#29a9e1"/></svg></span><div><h3>No sound / low audio</h3><p>Quick repair by certified techs using genuine parts.</p></div></div>
      <div class="service"><span class="service-icon"><svg width="9" height="11" viewBox="0 0 9 11"><rect x="0.5" y="4.5" width="8" height="6" fill="#29a9e1"/><path d="M2 4.5V3a2.5 2.5 0 015 0" stroke="#29a9e1" fill="none"/></svg></span><div><h3>Unlocking service</h3><p>Quick repair by certified techs using genuine parts.</p></div></div>
      <div class="service"><span class="service-icon"><svg width="11" height="10" viewBox="0 0 11 10"><path d="M0 3h3l3-3v10L3 7H0z" fill="#29a9e1"/><path d="M8 2a4 4 0 010 6" stroke="#29a9e1" fill="none"/></svg></span><div><h3>Volume Button</h3><p>Quick repair by certified techs using genuine parts.</p></div></div>
    </div>
  </div>
</section>

<section class="walkin">
  <h2>SAME DAY WALK IN NOVA PHONE REPAIRS BAY AREA</h2>
  <p class="sub">Walk in, walk out fixed</p>
  <div class="device-row">
    <div class="device"><div class="device-shot" role="img" aria-label="Nova Phone handset" style="width:52px;height:96px"></div><span>NOVA PHONE</span></div>
    <div class="device"><div class="device-shot" role="img" aria-label="Nova Tab tablet" style="width:74px;height:96px"></div><span>NOVA TAB</span></div>
    <div class="device"><div class="device-shot" role="img" aria-label="Nova Play media player" style="width:46px;height:96px"></div><span>NOVA PLAY</span></div>
    <div class="device"><div class="device-shot" role="img" aria-label="Nova Book laptop" style="width:100px;height:70px;margin-top:26px"></div><span>NOVA BOOK REPAIR</span></div>
  </div>
</section>

<section class="reviews">
  <h2 class="section-title">TRUSTED BY OVER 20 MILLION CUSTOMERS AND COUNTING.</h2>
  <div class="review-row">
    <div class="review"><div class="stars">★★★★★</div><p>Fast, friendly service and my screen looked brand new within the hour.</p><a href="#">Read more</a></div>
    <div class="review"><div class="stars">★★★★★</div><p>Fast, friendly service and my screen looked brand new within the hour.</p><a href="#">Read more</a></div>
    <div class="review"><div class="stars">★★★★★</div><p>Fast, friendly service and my screen looked brand new within the hour.</p><a href="#">Read more</a></div>
    <div class="review"><div class="stars">★★★★★</div><p>Fast, friendly service and my screen looked brand new within the hour.</p><a href="#">Read more</a></div>
  </div>
</section>

<section class="about">
  <div class="about-text">
    <h2>WHO WE ARE</h2>
    <p>Brisk Mend began as a single repair counter in the bay area and has grown into a group of trusted shops. Our certified technicians fix phones and tablets every day, and our protection plans now give families and businesses the same fast, careful care before anything breaks. We keep pricing clear and service honest.</p>
    <p>Corporate accounts get a dedicated contact, priority turnaround and simple monthly billing.</p>
    <span class="btn-dark">Enter More</span>
  </div>
  <div class="about-photo" role="img" aria-label="Photo of a smiling couple looking at a laptop together"></div>
</section>

<footer class="site-footer">
  <nav class="footer-links"><span>Home</span><span>About us</span><span>Repair</span><span>Protect</span><span>Contact</span><span>Support</span><span>Legal</span></nav>
  <div class="brand"><span class="brand-mark"></span>Brisk Mend</div>
</footer>

</body>
</html>
```